WINDOWSILL a novel

He loves her, she loves him, and they work in a bar in Covent Garden. He is American; she is British. Brexit has happened and they don't care. His wife has called from America (ex-wife) and they don't care. They don't care about much because they are in their bar, and their bar is their haven. Sometimes it's Velvet Hornet in there; sometimes it's the blues. They don't care. They are just a bit toooo cool, calm and collected. Let's send some wind up their sails.

Windowsill is the first in a three-part story about a man and a woman who love each other because life is simple. Music is important in the series, and music of the 70s, 80s and 90s. The covers have to capture their cool, easy way, and yet say "this is a love story". The books brings them their romance.

Author is Maren Tolsby.

Image ideas: a Covent Garden setting for literal. A mermaid for symbolic. A music note for metaphorical. A lily for beauty.

```html
<!DOCTYPE html>
<html lang="en">
<head>
<meta charset="utf-8">
<title>Windowsill — a novel by Maren Tolsby</title>
<link rel="stylesheet" href="https://fonts.googleapis.com/css2?family=Lustria&family=Caveat:wght@500&display=swap">
<style>
  :root {
    --night: #0d0d0e;
    --night-soft: #1e1e20;
    --ember: #e8363f;
    --ember-deep: #d42a35;
  }
  html, body {
    margin: 0;
    padding: 0;
    width: 791px;
    height: 1200px;
    overflow: hidden;
    background: var(--night);
  }
  .cover {
    position: relative;
    width: 791px;
    height: 1200px;
    overflow: hidden;
    background:
      linear-gradient(172deg, var(--night-soft) 0%, var(--night) 35%, #141416 60%, var(--night) 100%);
  }
  .night-sky {
    position: absolute;
    inset: 0;
    background:
      repeating-linear-gradient(170deg, rgba(255,255,255,0.025) 0 2px, transparent 2px 7px);
  }
  .title {
    position: absolute;
    right: 28px;
    margin: 0;
    font-family: "Lustria", Georgia, serif;
    font-weight: 400;
    color: var(--ember);
    text-align: right;
    line-height: 1;
  }
  .title span {
    display: block;
    font-size: 188px;
    letter-spacing: -3px;
  }
  .title .line-one { margin-top: 70px; }
  .title .line-two { margin-top: 40px; }
  .tagline {
    position: absolute;
    left: 396px;
    top: 668px;
    margin: 0;
    font-family: "Caveat", cursive;
    font-weight: 500;
    font-size: 74px;
    line-height: 1;
    color: var(--ember);
  }
  .author {
    position: absolute;
    right: 24px;
    top: 742px;
    margin: 0;
    font-family: "Lustria", Georgia, serif;
    font-weight: 400;
    font-size: 88px;
    line-height: 1;
    letter-spacing: -1px;
    color: var(--ember);
  }
  .hillside {
    position: absolute;
    left: 0;
    bottom: 0;
    width: 791px;
    height: 300px;
  }
</style>
</head>
<body>
  <main class="cover">
    <div class="night-sky" role="img" aria-label="Dark brushed night sky speckled with small white stars"></div>

    <h1 class="title">
      <span class="line-one">Window</span>
      <span class="line-two">sill</span>
    </h1>

    <p class="tagline">a novel by</p>
    <p class="author">Maren Tolsby</p>

    <svg class="hillside" viewBox="0 900 791 300" role="img" aria-label="Red grassy hilltop with the silhouettes of a man and a woman standing face to face">
      <path d="M170 1200 Q 420 1005 791 952 L791 1200 Z" fill="var(--ember-deep)"/>
    </svg>
  </main>
</body>
</html>
```